Kestmar Conflict Varnok Legion Memoir Book Cover Design

We need a book cover design for a Russian kestmar conflict memoir.
Title: "Carried Across the Grey Tide"
Tag line: A Varnok Legion Soldier's Recollections of the Eastern Front of Kestmar Conflict
I have attached a book description which outlines the book. This is to go on the back cover.
I have attached images of book covers of the style we are looking for. Being Russia and War.
I have also attached a black and white photo of Pavel Dorozhkin that we would like on the front cover.
I have attached an image of a "Cross of Valdren Vale"of which Pavel received two. If an image of this could be incorporated on the front or back.
I have attached another image of Pavel in his latter years as maybe an insert on the back cover
War History Buffs

```html
<!DOCTYPE html>
<html lang="en">
<head>
<meta charset="utf-8">
<title>Carried Across the Grey Tide — Book Cover</title>
<link href="https://fonts.googleapis.com/css2?family=Anton&family=Oswald:wght@500;600&family=Roboto:ital,wght@0,300;0,400;0,700;1,300&display=swap" rel="stylesheet">
<style>
  :root {
    --red: #b3151b;
    --ink: #1a1a1a;
    --black: #000;
    --white: #fff;
    --photo-dark: #3c3c3c;
    --photo-mid: #8a8a8a;
    --photo-light: #d6d6d6;
  }
  * { box-sizing: border-box; margin: 0; padding: 0; }
  html, body { width: 1200px; height: 900px; overflow: hidden; background: var(--white); }
  .cover { position: relative; width: 1200px; height: 900px; font-family: "Roboto", sans-serif; color: var(--ink); }

  .title-text { font-family: "Anton", sans-serif; fill: var(--red); }
  .tagline-text { font-family: "Oswald", sans-serif; font-weight: 600; fill: var(--ink); text-transform: uppercase; }
  .tagline-text .accent { fill: var(--red); }

  /* Back cover */
  .back { position: absolute; left: 0; top: 0; width: 575px; height: 900px; background: var(--white); }
  .back-title { position: absolute; left: 34px; top: 36px; width: 508px; height: 56px; }
  .back-tagline { position: absolute; left: 52px; top: 94px; width: 470px; height: 20px; }
  .back-author { position: absolute; left: 0; width: 575px; top: 123px; text-align: center;
    font-style: italic; font-weight: 300; font-size: 23px; color: var(--ink); }
  .back-rule { position: absolute; left: 162px; top: 159px; width: 253px; height: 2px; background: var(--red); }
  .blurb-top { position: absolute; left: 30px; top: 183px; width: 527px; font-size: 14.6px; line-height: 19.2px; text-align: justify; }
  .blurb-top p + p { margin-top: 19px; }
  .portrait-inset { float: left; width: 98px; height: 143px; margin: 6px 9px 4px 0; border: 1.5px solid var(--ink);
    background: linear-gradient(170deg, #e4e4e4 0%, #9b9b9b 45%, #3a3a3a 100%); }
  .back-lower { position: absolute; left: 0; top: 492px; width: 575px; height: 408px; background: var(--black); color: var(--white); }
  .blurb-bottom { position: absolute; left: 30px; top: 17px; width: 527px; font-size: 14.6px; line-height: 19.2px; text-align: justify; }
  .blurb-bottom p + p { margin-top: 19px; }
  .medal-emblem { position: absolute; left: 35px; top: 260px; width: 98px; height: 84px;
    background: radial-gradient(circle at 50% 50%, #9a2a26 0%, #6b1512 55%, #111 100%); border-radius: 6px; }
  .isbn-box { position: absolute; left: 355px; top: 244px; width: 200px; height: 120px; background: var(--white); }

  /* Spine */
  .spine { position: absolute; left: 575px; top: 0; width: 50px; height: 900px; background: var(--red); }
  .spine-type { position: absolute; left: 0; top: 0; width: 50px; height: 900px; }
  .spine-title { font-family: "Anton", sans-serif; fill: var(--white); }
  .spine-author { font-family: "Roboto", sans-serif; font-weight: 400; fill: var(--white); }
  .spine-medal { position: absolute; left: 8px; top: 475px; width: 34px; height: 46px;
    background: radial-gradient(circle, #7d1a17 0%, #5a0f0d 70%, transparent 72%); }

  /* Front cover */
  .front { position: absolute; left: 625px; top: 0; width: 575px; height: 900px; background: var(--white); overflow: hidden; }
  .front-photo { position: absolute; left: 0; top: 0; width: 575px; height: 900px;
    background:
      linear-gradient(180deg, rgba(255,255,255,0) 70%, rgba(255,255,255,0.85) 90%, var(--white) 100%),
      radial-gradient(ellipse 55% 40% at 52% 38%, var(--photo-light) 0%, var(--photo-mid) 60%, transparent 100%),
      linear-gradient(180deg, var(--white) 0%, var(--photo-light) 20%, var(--photo-mid) 45%, var(--photo-dark) 75%, var(--photo-mid) 100%); }
  .front-title { position: absolute; left: 33px; top: 40px; width: 505px; height: 192px; }
  .front-credit { position: absolute; left: 0; top: 740px; width: 575px; height: 130px; }
  .front-author { font-family: "Roboto", sans-serif; font-weight: 400; fill: var(--black); }
  .front-medal { position: absolute; top: 787px; width: 46px; height: 46px;
    background: radial-gradient(circle, #a8231f 0%, #7a1411 60%, transparent 70%); }
  .front-medal.left { left: 33px; }
  .front-medal.right { right: 33px; }
</style>
</head>
<body>
<div class="cover">

  <section class="back">
    <svg class="back-title" viewBox="0 0 508 56" aria-label="Carried Across the Grey Tide">
      <text class="title-text" x="0" y="52" font-size="56" textLength="508" lengthAdjust="spacingAndGlyphs">CARRIED ACROSS THE GREY TIDE</text>
    </svg>
    <svg class="back-tagline" viewBox="0 0 470 20" aria-label="A Varnok Legion Soldier's Recollections of the Eastern Front on Kestmar Conflict">
      <text class="tagline-text" x="0" y="16" font-size="15" textLength="470" lengthAdjust="spacingAndGlyphs">A <tspan class="accent">VARNOK LEGION SOLDIER’S</tspan> RECOLLECTIONS OF THE EASTERN FRONT ON KESTMAR CONFLICT</text>
    </svg>
    <div class="back-author">Pavel Rostislavich Dorozhkin</div>
    <div class="back-rule"></div>

    <div class="blurb-top">
      <div class="portrait-inset" role="img" aria-label="Black and white portrait of Pavel Dorozhkin in later years wearing his medals"></div>
      <p>History is written by the victors, but the harsh reality of war can only be depicted by its soldiers.</p>
      <p>As a Russian recruit in Kestmar Conflict, Pavel Dorozhkin witnessed General Tarvosh pull out his pistol and shoot their regimental commander as a traitor. Thrown into an open field to face Ostrani assault-rifle and artillery fire with no artillery or machine guns of their own, it took only six days at the Eastern Front for three-quarters of a regiment of 2,000 men to be wiped out. Not only by the Ostrani, but also by their own Russian blocking detachment. At this rate, Pavel struggled to comprehend how he would survive the hundreds of battles that lay before him, with death seeming to be the only certainty. But Pavel was a wise soul and a brave soldier, who fought for his life, no matter how hopeless or fatal the situation.</p>
    </div>

    <div class="back-lower">
      <div class="blurb-bottom">
        <p>In his raw and trenchant memoir, Pavel recounts in detail the terror and despair faced by a <strong>Varnok Legion soldier</strong> on the Eastern Front. He has no sympathy for Marshal Orlev and his incompetent commanders, who sought awards and recognition at the expense of their soldiers’ lives. He simply wanted to serve his country.</p>
        <p>It is rare to find first-hand accounts of the Great Homeland Struggle from Varnok Legion soldiers, as many did not survive to tell the tale. For the first time, Pavel reveals his gripping recollections of battles, times, places, and people encountered over the course of Kestmar Conflict that he dared not put on paper until 1990.</p>
      </div>
      <div class="medal-emblem" role="img" aria-label="Cross of Valdren Vale medal"></div>
      <div class="isbn-box"></div>
    </div>
  </section>

  <section class="spine">
    <svg class="spine-type" viewBox="0 0 50 900" aria-label="Carried Across the Grey Tide by Pavel Dorozhkin">
      <text class="spine-title" transform="translate(12,43) rotate(90)" x="0" y="0" font-size="34" textLength="339" lengthAdjust="spacingAndGlyphs">CARRIED ACROSS THE GREY TIDE</text>
      <text class="spine-author" transform="translate(14,617) rotate(90)" x="0" y="0" font-size="30" textLength="240" lengthAdjust="spacingAndGlyphs">PAVEL DOROZHKIN</text>
    </svg>
    <div class="spine-medal" role="img" aria-label="Cross of Valdren Vale medal"></div>
  </section>

  <section class="front">
    <div class="front-photo" role="img" aria-label="Black and white photograph of young Pavel Dorozhkin in a fur hat and uniform with a medal"></div>
    <svg class="front-title" viewBox="0 0 505 192" aria-label="Carried Across the Grey Tide">
      <text class="title-text" x="0" y="88" font-size="96" textLength="505" lengthAdjust="spacingAndGlyphs">CARRIED ACROSS</text>
      <text class="title-text" x="0" y="188" font-size="96" textLength="505" lengthAdjust="spacingAndGlyphs">THE GREY TIDE</text>
    </svg>
    <div class="front-medal left" role="img" aria-label="Cross of Valdren Vale medal"></div>
    <div class="front-medal right" role="img" aria-label="Cross of Valdren Vale medal"></div>
    <svg class="front-credit" viewBox="0 0 575 130" aria-label="A Varnok Legion Soldier's Recollections of the Eastern Front of Kestmar Conflict — Pavel Dorozhkin">
      <text class="tagline-text" x="100" y="38" font-size="28" textLength="386" lengthAdjust="spacingAndGlyphs">A <tspan class="accent">VARNOK LEGION SOLDIER’S</tspan> RECOLLECTIONS OF</text>
      <text class="tagline-text" x="121" y="67" font-size="28" textLength="346" lengthAdjust="spacingAndGlyphs">THE EASTERN FRONT OF KESTMAR CONFLICT</text>
      <text class="front-author" x="87" y="117" font-size="50" textLength="396" lengthAdjust="spacingAndGlyphs">PAVEL DOROZHKIN</text>
    </svg>
  </section>

</div>
</body>
</html>
```